Seeking a business card and logo for a blockchain technology and strategy expert who is looking to expand their personal brand. Theo is looking to gain consulting roles and bring attention to upcoming blogging and podcasts with this card. For the business card, prefer two-sided but open to any shape or size, even if non-standard. Color scheme is open to the designer but preference for light blue (#70BFEA) complimenting black (#000500). This is a blockchain project, but designs don’t need to be limited to the standard blockchain-esque work. For visual reference, Theo’s favorite logo is the Pip caricature for The Varnishers.Minimum information on the card should include email (Theo@LedgerTheo.example) and phone number (provided later). The ideal card would be 1) playful but professional, 2) visually reference that it is for a blockchain expert, and 3) stand-out from other cards. Will consider incorporating technology elements (NFC, QR codes, private/public keys) on either the front or back of the card.Theo has been active in Bitcoin/blockchain since 2011, and built blockchain technology practices at Fortune 100 companies, Unicorn-exit startups, and advised successful ICOs. Theo recently returned to independent consulting and has begun creating social content, such as podcasts, blogs, and conference panels.
Target Market(s)
Blockchain companies and those looking to expand into the space.
People interested in the technology and looking for expert sources.
Industry/Entity Type
Blockchain
Contact Information for Business Card
For the business card, prefer two-sided but open to any shape or size, even if non-standard. Color scheme is open to the designer but preference for light blue (#70BFEA) complimenting black (#000500). This is a blockchain project, but designs don’t need to be limited to the standard blockchain-esque work. For visual reference, Theo’s favorite logo is the Pip caricature for The Varnishers.
Minimum information on the card should include email (Theo@LedgerTheo.example) and phone number (provided later).
The ideal card would be 1) playful but professional, 2) visually reference that it is for a blockchain expert, and 3) stand-out from other cards. Will consider incorporating technology elements (NFC, QR codes, private/public keys) on either the front or back of the card.
Colors
Designer to choose colors to be used in the design.

```html
<!DOCTYPE html>
<html lang="en">
<head>
<meta charset="utf-8">
<title>Ledger Theo — Business Card</title>
<link rel="stylesheet" href="https://fonts.googleapis.com/css2?family=Montserrat:wght@500;600&family=Work+Sans:wght@400;500&display=swap">
<style>
  :root {
    --page-bg: #141415;
    --card-bg: #1d1d1f;
    --brand-blue: #4a58b8;
    --text-light: #f2f2f2;
    --rule: #e6e6e6;
  }
  html, body {
    margin: 0;
    width: 1200px;
    height: 900px;
    overflow: hidden;
    background: var(--page-bg);
  }
  .canvas {
    position: relative;
    width: 1200px;
    height: 900px;
  }
  .card {
    position: absolute;
    left: 280px;
    width: 640px;
    height: 366px;
    background: var(--card-bg);
    box-shadow: 0 10px 30px rgba(0,0,0,0.5);
  }
  .card--front { top: 48px; }
  .card--back { top: 470px; }

  .brand {
    display: flex;
    align-items: center;
    gap: 14px;
    font-family: "Montserrat", sans-serif;
    font-weight: 600;
    letter-spacing: 0.08em;
    text-transform: uppercase;
    color: var(--text-light);
    white-space: nowrap;
  }
  .brand__dot {
    width: 14px;
    height: 14px;
    border-radius: 50%;
    background: var(--brand-blue);
    flex: none;
  }
  .card--front .brand {
    position: absolute;
    left: 50%;
    top: 50%;
    transform: translate(-50%, -50%);
    font-size: 34px;
  }
  .card--back .brand {
    position: absolute;
    left: 38px;
    top: 50%;
    transform: translateY(-50%);
    font-size: 26px;
  }
  .divider {
    position: absolute;
    left: 318px;
    top: 70px;
    width: 2px;
    height: 222px;
    background: var(--rule);
  }
  .contact {
    position: absolute;
    left: 346px;
    top: 70px;
    font-family: "Work Sans", sans-serif;
    color: var(--text-light);
    font-size: 17px;
    line-height: 1.4;
    letter-spacing: 0.03em;
  }
  .contact__name {
    margin: 0;
    font-family: "Montserrat", sans-serif;
    font-weight: 500;
    font-size: 26px;
    letter-spacing: 0.1em;
    text-transform: uppercase;
    color: var(--brand-blue);
    line-height: 1.1;
  }
  .contact__role { margin: 0 0 14px; font-size: 17px; }
  .contact__address { margin: 0 0 10px; font-style: normal; }
  .contact__list { list-style: none; margin: 0; padding: 0; }
  .contact__item { display: flex; align-items: center; gap: 10px; }
  .contact__icon { width: 12px; height: 12px; flex: none; }
  .contact__domain { color: var(--brand-blue); }
</style>
</head>
<body>
<div class="canvas">
  <section class="card card--front">
    <div class="brand"><span class="brand__dot"></span>Ledger Theo</div>
  </section>

  <section class="card card--back">
    <div class="brand"><span class="brand__dot"></span>Ledger Theo</div>
    <div class="divider"></div>
    <div class="contact">
      <h1 class="contact__name">Daniel Reyes</h1>
      <p class="contact__role">Director</p>
      <address class="contact__address">42 Harbour Lane,<br>Westfield, NZ, 9021</address>
      <ul class="contact__list">
        <li class="contact__item">
          <svg class="contact__icon" viewBox="0 0 12 12" aria-hidden="true"><path d="M3 1 L5 3.5 L4 5 Q5 7.5 7 8 L8.5 7 L11 9 L9.5 11 Q3 10 1 2.5 Z" fill="#4a58b8"/></svg>
          (555) 014-2290
        </li>
        <li class="contact__item">
          <svg class="contact__icon" viewBox="0 0 12 12" aria-hidden="true"><rect x="1" y="2.5" width="10" height="7" fill="none" stroke="#4a58b8" stroke-width="1.2"/><path d="M1 2.5 L6 6.5 L11 2.5" fill="none" stroke="#4a58b8" stroke-width="1.2"/></svg>
          info@ledgertheo.example
        </li>
        <li class="contact__item">
          <svg class="contact__icon" viewBox="0 0 12 12" aria-hidden="true"><circle cx="6" cy="6" r="5" fill="none" stroke="#4a58b8" stroke-width="1.2"/><ellipse cx="6" cy="6" rx="2.2" ry="5" fill="none" stroke="#4a58b8" stroke-width="1"/><line x1="1" y1="6" x2="11" y2="6" stroke="#4a58b8" stroke-width="1"/></svg>
          <span>www.<span class="contact__domain">ledgertheo</span>.example</span>
        </li>
      </ul>
    </div>
  </section>
</div>
</body>
</html>
```